Cobalt Ridge

Build a simple scrollable "floating" website - Website should have polished, modern look.
Domain has been bought on NestRoster and website should be setup there.
Project Brief:
https://slides.quorvane.com/deck/7Kp2Xa9Lm4Qe8Rt1Vb6Nc3Hz5Wy0Jd/edit?share=open
Input Files:
https://www.filtravo.com/f/k3mp81zt07qvr5n/BBDXnaQGyTsC_prLJFHK8u3xb?get=0

Build

```html
<!DOCTYPE html>
<html lang="en">
<head>
<meta charset="utf-8">
<title>Cobalt Ridge – Coastline Circuit</title>
<link rel="stylesheet" href="https://fonts.googleapis.com/css2?family=Poppins:wght@300;400;500;600&display=swap">
<style>
:root{
  --teal:#0f6f78;
  --orange:#c8430f;
  --ink:#2d3138;
  --muted:#6b6f76;
  --page:#f6f6f5;
  --band:#e9ebef;
  --footer:#3f4550;
  --line:#d5d7da;
  --badge:#9aa0a7;
}
*{box-sizing:border-box;margin:0;padding:0}
html,body{width:1200px;height:2757px;overflow:hidden}
body{position:relative;background:var(--page);font-family:"Poppins",sans-serif;color:var(--ink)}
.abs{position:absolute}
.photo{position:absolute}
/* hero */
.hero-bg{left:0;top:0;width:1200px;height:482px;background:linear-gradient(135deg,#6a5a4a,#9c8a72 45%,#4d5a3c)}
.logo{left:156px;top:18px;width:96px;height:96px;border-radius:50%;background:var(--teal);border:4px solid #fff;display:flex;align-items:center;justify-content:center;text-align:center;color:#fff;font-size:11px;font-weight:600;line-height:1.2;padding:10px}
.nav{left:334px;top:52px;font-size:11.5px;color:#fff}
.nav a{color:#fff;text-decoration:none;position:absolute;white-space:nowrap}
.login{left:932px;top:48px;width:112px;height:33px;background:var(--orange);color:#fff;font-size:11px;font-weight:600;display:flex;align-items:center;justify-content:center;gap:6px}
.slide{left:156px;top:129px;width:888px;height:398px;background:linear-gradient(120deg,#7b6a55,#a99378 40%,#7d6b56 70%,#3f5a34);box-shadow:0 14px 24px rgba(0,0,0,.18)}
.slide h1{position:absolute;left:76px;top:116px;font-size:28px;font-weight:600;color:#fff;line-height:1.25;white-space:nowrap}
.btn{display:flex;align-items:center;justify-content:center;color:#fff;font-size:11px;font-weight:600;text-transform:uppercase;letter-spacing:.3px}
.btn-teal{background:var(--teal)}
.btn-orange{background:var(--orange)}
.dots{left:957px;top:281px;display:flex;flex-direction:column;gap:14px}
.dots span{width:9px;height:9px;border-radius:50%;background:#fff}
/* section titles */
.title{left:0;width:1200px;display:flex;align-items:center;justify-content:center;gap:18px;font-size:23px;font-weight:400;color:var(--ink);white-space:nowrap}
.title::before,.title::after{content:"";width:76px;height:1px;background:#777}
.title b{color:var(--teal);font-weight:600}
/* trash grid */
.tile{position:absolute}
.tile-feature{background:var(--orange);display:flex;flex-direction:column;align-items:center;justify-content:center;color:#fff;font-size:13.5px;font-weight:600;text-align:center;line-height:1.3;gap:20px}
/* data cards */
.card{position:absolute;top:1310px;width:384px;height:199px;color:#fff;text-align:center;padding-top:26px}
.card h3{font-size:17px;font-weight:600;line-height:1.3}
.card .dash{font-size:14px;line-height:1;margin:2px 0 8px}
.card p{font-size:12.5px;line-height:1.4;width:260px;margin:0 auto}
.card .dl{margin:26px auto 0;width:128px;height:34px;font-size:11px;font-weight:500;display:flex;align-items:center;justify-content:center;gap:6px;text-transform:uppercase}
.card-teal{background:var(--teal)}
.card-teal .dl{border:1px solid #fff;color:#fff}
.card-orange{background:var(--orange)}
.card-orange .dl{background:#fff;color:var(--orange)}
/* expedition */
.lede{left:300px;top:1608px;width:600px;text-align:center;font-size:14.5px;font-weight:300;line-height:1.65;color:var(--muted)}
.video{left:232px;top:1733px;width:737px;height:318px;background:linear-gradient(160deg,#3f5a3a,#6e6a5e 45%,#8b8578 70%,#3d4c55);box-shadow:0 14px 24px rgba(0,0,0,.15)}
/* partners */
.partners{left:0;top:2108px;width:1200px;height:175px;background:var(--band)}
.partners h2{position:absolute;left:156px;top:26px;font-size:23px;font-weight:400;display:flex;align-items:center;gap:14px;white-space:nowrap}
.partners h2 b{color:var(--teal);font-weight:600}
.partners h2::after{content:"";width:76px;height:1px;background:#777}
.partner{position:absolute;top:88px;width:170px;height:60px;display:flex;align-items:center;justify-content:center;font-size:17px;font-weight:500;color:var(--ink);white-space:nowrap;text-align:center}
.partner .badge{width:58px;height:58px;border-radius:50%;background:var(--badge)}
/* contact */
.field{position:absolute;background:#fff;border:1px solid var(--line);font-size:11px;color:#9a9da2;padding:10px 14px}
/* footer */
.footer{left:0;top:2693px;width:1200px;height:64px;background:var(--footer);color:#fff;font-size:11px}
.footer .copy{position:absolute;left:156px;top:25px}
.footer .social{position:absolute;left:822px;top:25px}
.sq{position:absolute;top:16px;width:30px;height:30px}
.up{position:absolute;left:993px;top:0;width:51px;height:64px;background:var(--orange);display:flex;align-items:center;justify-content:center}
</style>
</head>
<body>

<!-- header & hero -->
<div class="photo hero-bg" role="img" aria-label="Blurred backdrop photo of a rocky coastal cliff"></div>
<div class="abs logo">Coastline Circuit</div>
<nav class="abs nav">
  <a style="left:0">-- Home ▾</a>
  <a style="left:94px">Trash Sites</a>
  <a style="left:193px">Raw Data</a>
  <a style="left:285px">Expedition</a>
  <a style="left:383px">Supporters</a>
  <a style="left:482px">Get in Touch</a>
</nav>
<div class="abs login">
  <svg width="11" height="11" viewBox="0 0 12 12"><circle cx="6" cy="6" r="5.2" fill="none" stroke="#fff" stroke-width="1.3"/><circle cx="6" cy="4.8" r="1.8" fill="#fff"/><path d="M2.8 9.6a3.6 3.6 0 0 1 6.4 0" fill="#fff"/></svg>LOGIN
</div>
<section class="abs slide" role="img" aria-label="Photo of two climbers with backpacks scrambling up a coastal rock face">
  <h1>The Data Was Recorded<br>During the 2017 Coastline Circuit<br>Expedition.</h1>
  <div class="abs btn btn-teal" style="left:76px;top:244px;width:126px;height:33px">Contact Us</div>
</section>
<div class="abs dots"><span></span><span style="background:var(--orange)"></span><span></span><span></span><span></span></div>

<!-- trash sites -->
<h2 class="abs title" style="top:568px"><span>Trash <b>Sites</b></span></h2>
<div class="tile" role="img" aria-label="Photo of fishing nets and debris washed up on a beach" style="left:156px;top:627px;width:280px;height:158px;background:linear-gradient(180deg,#6fa4c8 0 30%,#6a8a6e 30%,#8a7f5e)"></div>
<div class="tile" role="img" aria-label="Photo of a volunteer collecting trash on rocks near power station chimneys" style="left:156px;top:811px;width:280px;height:334px;background:linear-gradient(180deg,#9ab8d8 0 35%,#4e5a4a 35%,#7a7266)"></div>
<div class="tile tile-feature" style="left:460px;top:627px;width:279px;height:334px">
  <span>Contrary to popular belief<br>Lorem Ipsum</span>
  <svg width="18" height="18" viewBox="0 0 18 18" fill="none" stroke="#fff" stroke-width="2"><rect x="2" y="6" width="8" height="5" rx="2.5" transform="rotate(45 6 8.5)"/><rect x="8" y="7" width="8" height="5" rx="2.5" transform="rotate(45 12 9.5)"/></svg>
</div>
<div class="tile" role="img" aria-label="Photo of volunteers hauling fishing nets on a beach" style="left:460px;top:987px;width:279px;height:158px;background:linear-gradient(180deg,#b9d6e4 0 30%,#7fb8b8 30%,#d2c6aa)"></div>
<div class="tile" role="img" aria-label="Photo of plastic bottles scattered along a shoreline" style="left:765px;top:627px;width:279px;height:158px;background:linear-gradient(180deg,#c9d4dc 0 35%,#6d7470 35%,#4f8a5a)"></div>
<div class="tile" role="img" aria-label="Photo of volunteers sorting plastic waste on a beach" style="left:765px;top:811px;width:279px;height:334px;background:linear-gradient(180deg,#b8cdd9 0 30%,#a8a296 30%,#7f7a72)"></div>
<div class="abs btn btn-teal" style="left:544px;top:1180px;width:112px;height:31px;font-size:10px">Load More</div>

<!-- data & research -->
<h2 class="abs title" style="top:1253px"><span>Data &amp; <b>Research</b></span></h2>
<div class="card card-teal" style="left:0">
  <h3>Water Pollution</h3><div class="dash">---</div>
  <p>There are many variations lorem Lorem ipsum dolor sit amet of Lorem</p>
  <div class="dl"><svg width="10" height="10" viewBox="0 0 10 10"><path d="M5 1v6M2 4.5 5 7.5 8 4.5M1 9h8" stroke="currentColor" stroke-width="1.5" fill="none"/></svg>Download</div>
</div>
<div class="card card-orange" style="left:408px">
  <h3>BioChemistry Data</h3><div class="dash">---</div>
  <p>There are many variations lorem Lorem ipsum dolor sit amet of Lorem</p>
  <div class="dl"><svg width="10" height="10" viewBox="0 0 10 10"><path d="M5 1v6M2 4.5 5 7.5 8 4.5M1 9h8" stroke="currentColor" stroke-width="1.5" fill="none"/></svg>Download</div>
</div>
<div class="card card-teal" style="left:816px;padding-top:24px">
  <h3>Reasearch Report by<br>Harbourview University</h3>
  <p style="margin-top:8px">There are many variations lorem Lorem ipsum dolor sit amet of Lorem</p>
  <div class="dl"><svg width="10" height="10" viewBox="0 0 10 10"><path d="M5 1v6M2 4.5 5 7.5 8 4.5M1 9h8" stroke="currentColor" stroke-width="1.5" fill="none"/></svg>Download</div>
</div>

<!-- expedition -->
<h2 class="abs title" style="top:1549px"><span>The <b>Expedition</b></span></h2>
<p class="abs lede">In May 2017 Mara Lindqvist and Tomas Verhey completed the first successful coasteering expedition of the island. In 6 days they climbed, swam, scrambled and hiked the entire coastline, took 51 water samples and mapped 163 trash pollution spots</p>
<div class="abs video" role="img" aria-label="Video still of a rocky coastline with climbers beside the sea">
  <svg class="abs" style="left:340px;top:131px" width="56" height="56" viewBox="0 0 56 56"><circle cx="28" cy="28" r="25" fill="none" stroke="#fff" stroke-width="2.5"/><path d="M22 17 L39 28 L22 39Z" fill="#fff"/></svg>
</div>

<!-- partners -->
<section class="abs partners">
  <h2>Our <b>Partners</b></h2>
  <div class="partner" style="left:135px"><span class="badge" role="img" aria-label="Partner badge"></span></div>
  <div class="partner" style="left:279px">Halvane</div>
  <div class="partner" style="left:448px;font-size:15px">Tidemark Alliance</div>
  <div class="partner" style="left:639px">Northcrest</div>
  <div class="partner" style="left:842px;width:190px;font-size:15px">Harbourview University</div>
</section>

<!-- contact -->
<h2 class="abs title" style="top:2326px"><span>Get in <b>Touch</b></span></h2>
<div class="field" style="left:327px;top:2384px;width:265px;height:33px">Name*</div>
<div class="field" style="left:607px;top:2384px;width:264px;height:33px">E-mail*</div>
<div class="field" style="left:327px;top:2433px;width:265px;height:33px">phone</div>
<div class="field" style="left:607px;top:2433px;width:264px;height:33px">Subject</div>
<div class="field" style="left:327px;top:2483px;width:544px;height:110px">Message ...</div>
<div class="abs btn btn-orange" style="left:551px;top:2612px;width:96px;height:31px;gap:6px">
  <svg width="11" height="11" viewBox="0 0 12 12"><path d="M1 6 L11 1 L8 11 L6 7Z" fill="#fff"/></svg>Send
</div>

<!-- footer -->
<footer class="abs footer">
  <span class="copy">© 2017 <u>Coastline Circuit</u>. All Rights Reserved.</span>
  <span class="social">Get Social:</span>
  <span class="sq" style="left:897px;background:#3b5a98" aria-label="Social profile one"></span>
  <span class="sq" style="left:934px;background:#1d7ab5" aria-label="Social profile two"></span>
  <div class="up"><svg width="14" height="14" viewBox="0 0 14 14"><path d="M7 2 L7 12 M3 6 L7 2 L11 6" stroke="#fff" stroke-width="2.2" fill="none"/></svg></div>
</footer>

</body>
</html>
```